Alternative Health Practice - Website redesign

With regard to the welcome image, stock photos can't show the faces of other people. And please don't submit a design for a one-page website.
Hello, I am redesigning a website and need some help from a professional.
The old website is here: peter-lindqvist.net (pls note I don't want to reuse the welcome photo from the old site). Much of the written content will remain the same, so note that I also need a page layout/text colour etc that works for text heavy pages: ie www.peter-lindqvist.net/somatic-articles and www.peter-lindqvist.net/client-reviews
My effort at redesigning is underway here: https://pjlindqvist.sitebuilderhost.net/my-site-7
The original sitebuilder template is this one: https://www.sitebuilderhost.net/website-template/view/html/4917?originUrl=https%3A%2F%2Fwww.sitebuilderhost.net%2Fwebsite%2Ftemplates%2Fhtml%2Fhealth-wellness&tpClick=view_button&esi=8a41c27d-03e9-4c6b-b1f2-9d5e02a7c4f3
I'm pretty happy with the colour palette. My name Peter Joseph Lindqvist is now the "brand" without Rooted Stillness subtitle. Regarding the Welcome section, if you are going to use my photos, it probably needs to be those two that are already there. If you want to put a stock photo there instead, that's fine.
If you want to propose something quite different to my design, I'm happy to receive design files in Photoshop or whatever and then subsequently replicate on Sitebuilder. Up to you.
Mostly women, some men ages 28-60.

```html
<!DOCTYPE html>
<html lang="en">
<head>
<meta charset="utf-8">
<title>Peter Lindqvist – Energy Healing</title>
<link href="https://fonts.googleapis.com/css2?family=Khand:wght@500;600&family=Questrial&display=swap" rel="stylesheet">
<style>
:root{
  --bg:#0b0b0b;
  --gold:#c9a24a;
  --gold-light:#dcbc6c;
  --gold-dark:#b38c3a;
  --white:#ffffff;
  --cream:#e4dab9;
  --ink:#1a1a1a;
  --heading:"Khand",sans-serif;
  --body:"Questrial",sans-serif;
}
*{margin:0;padding:0;box-sizing:border-box}
html,body{width:1200px;height:2440px;overflow:hidden;background:var(--bg)}
body{position:relative;font-family:var(--body);color:var(--white)}
.abs{position:absolute}
.btn{position:absolute;display:flex;align-items:center;justify-content:center;border-radius:28px;
  background:linear-gradient(180deg,var(--gold-light),var(--gold-dark));color:var(--ink);
  font-family:var(--body);font-size:17px;letter-spacing:.5px;font-weight:700}
.heading{font-family:var(--heading);font-weight:600;line-height:1;letter-spacing:.5px}
.gold{color:var(--gold)}
.rule{position:absolute;height:2px;width:59px;background:var(--gold)}

/* header */
.brand{left:133px;top:62px;display:flex;align-items:center;gap:10px}
.brand-dot{width:22px;height:22px;border-radius:50%;background:var(--gold)}
.brand-name{font-family:var(--body);font-size:24px;letter-spacing:2px;color:var(--white);text-transform:uppercase}
.call{left:755px;top:18px;display:flex;align-items:center;gap:14px}
.icon-circle{width:40px;height:40px;border-radius:50%;background:var(--gold);display:flex;align-items:center;justify-content:center}
.call small{display:block;font-size:13px}
.call strong{display:block;font-size:16px;letter-spacing:.5px}
.lang{left:1010px;top:38px;font-size:13px;font-weight:700}
.lang .sep{color:var(--gold);margin:0 4px}
.nav{left:554px;top:87px;display:flex;gap:36px;font-size:14.5px}
.nav .active{color:var(--gold)}

/* hero */
.hero-title{left:134px;top:170px;font-size:56px}
.hero-title span{display:block;height:58px}
.hero-photo{left:570px;top:129px;width:497px;height:331px;
  background:linear-gradient(135deg,#8d8a7c 0%,#c8beb0 35%,#3a3350 65%,#5b4f72 100%)}
.dots{left:795px;top:445px;display:flex;gap:4px}
.dots i{width:9px;height:9px;border-radius:50%;background:var(--gold);border:1px solid #fff}
.dots i:nth-child(2){background:#fff}

/* energy */
.emblem{left:150px;top:531px;width:416px;height:416px;border-radius:50%;
  background:radial-gradient(circle at 50% 45%,#c98a4a 0%,#b9a88c 40%,#5a5346 75%,#0b0b0b 100%)}
.section-title{font-size:56px}
.copy{font-size:14px;line-height:26px}

/* cards */
.card{position:absolute;top:1146px;width:454px;height:201px;border:1px solid var(--gold);border-radius:2px}
.avatar{position:absolute;top:-38px;left:18px;width:76px;height:76px;border-radius:50%;border:2px solid #fff;
  background:linear-gradient(160deg,#6b4a3a,#c79a7f)}
.card p{position:absolute;left:24px;top:56px;width:410px;font-size:13.6px;line-height:25.5px}
.card .who{position:absolute;left:24px;top:166px;color:var(--gold);font-size:17px;font-weight:700;line-height:20px}
.quote{position:absolute;right:18px;bottom:17px}

/* about */
.portrait{left:748px;top:1506px;width:452px;height:600px;
  background:linear-gradient(180deg,#1c1a15 0%,#4a4734 40%,#5d5a43 70%,#3e3c2d 100%)}
.study{font-size:14px;line-height:26px}

/* footer */
.footer-shape{left:0;top:2030px}
.footer-mark{left:549px;top:1989px;width:104px;height:104px;border-radius:50%;background:var(--ink)}
.footer-brand{left:0;width:1200px;top:2112px;text-align:center;color:var(--ink)}
.footer-brand .name{font-size:40px;letter-spacing:4px;text-transform:uppercase}
.footer-nav{left:0;width:1200px;top:2201px;display:flex;justify-content:center;gap:36px;font-size:15px;color:var(--ink)}
.divider{left:133px;width:936px;height:1px;background:#b9ad88}
.contact{display:flex;align-items:center;gap:14px;color:var(--ink);font-size:14.5px;line-height:23px}
.contact strong{font-size:17px;letter-spacing:.5px}
.social{width:31px;height:31px;border:1.5px solid var(--ink)}
</style>
</head>
<body>

<header>
  <div class="abs brand"><span class="brand-dot"></span><span class="brand-name">Peter Lindqvist</span></div>
  <div class="abs call">
    <span class="icon-circle"><svg width="20" height="20" viewBox="0 0 24 24" fill="none" stroke="#fff" stroke-width="1.6"><path d="M5 3h4l2 5-2.5 1.5a11 11 0 0 0 6 6L16 13l5 2v4a2 2 0 0 1-2 2A16 16 0 0 1 3 5a2 2 0 0 1 2-2z"/></svg></span>
    <div><small>Call Us</small><strong>(+351) 91 204 7730</strong></div>
  </div>
  <div class="abs lang"><span class="gold">EN</span><span class="sep">|</span>ES</div>
  <nav class="abs nav"><span class="active">The Practice</span><span>About Me</span><span>Feedback</span><span>Approach</span><span>Contact Me</span></nav>
</header>

<section class="hero">
  <h1 class="abs heading hero-title"><span class="gold">Providing Rooted</span><span class="gold">Stillness</span><span>Energy Healing</span></h1>
  <div class="btn" style="left:133px;top:363px;width:200px;height:52px">BOOK A SESSION</div>
  <div class="abs hero-photo" role="img" aria-label="Practitioner's hands resting on a client's leg during an energy healing session"></div>
  <div class="abs dots"><i></i><i></i><i></i><i></i></div>
</section>

<section class="energy">
  <div class="abs emblem" role="img" aria-label="Round decorative cut-out showing a healing session photo"></div>
  <h2 class="abs heading section-title" style="left:600px;top:588px">ENERGY <span class="gold">HEALING</span></h2>
  <div class="rule" style="left:600px;top:648px"></div>
  <div class="abs copy" style="left:600px;top:664px;width:460px">
    <p>A session typically begins by clarifying your intention or wish. You may be facing physical or emotional challenges or seeking help with another aspect of your life, such as family or relationship problems.</p>
    <p style="margin-top:4px">With your interest in the work clarified, I will assess how energy is flowing in your body and where there are blockages in the physical structure.</p>
  </div>
  <div class="btn" style="left:600px;top:840px;width:168px;height:51px">KNOW MORE</div>
</section>

<section class="experiences">
  <h2 class="abs heading section-title" style="left:0;width:1200px;text-align:center;top:1032px">CUSTOMER <span class="gold">EXPERIENCES</span></h2>
  <div class="rule" style="left:571px;top:1093px"></div>

  <article class="card" style="left:134px">
    <div class="avatar" role="img" aria-label="Client portrait"></div>
    <p>You have given me a lot of confidence in myself. You are showing me a new way of life. And I've learned that it is possible to handle the physical pain caused by our emotions. I didn't know how to cope with it.&nbsp; Thank you...</p>
    <span class="who">Marta Oliveira Ruiz</span>
    <svg class="quote" width="44" height="36" viewBox="0 0 44 36" fill="#4a4a4a"><path d="M0 0h18v22a14 14 0 0 1-14 14H0v-8h4a6 6 0 0 0 6-6H0zM26 0h18v22a14 14 0 0 1-14 14h-4v-8h4a6 6 0 0 0 6-6H26z"/></svg>
  </article>

  <article class="card" style="left:614px">
    <div class="avatar" role="img" aria-label="Client portrait" style="background:linear-gradient(160deg,#3a5fb0,#d9b98f)"></div>
    <p style="width:400px;left:28px">I discovered Rooted Stillness 2 years ago and it amazes me how it has changed my approach to many aspects of my life.</p>
    <span class="who">Claire Dumontet</span>
    <svg class="quote" width="44" height="36" viewBox="0 0 44 36" fill="#4a4a4a"><path d="M0 0h18v22a14 14 0 0 1-14 14H0v-8h4a6 6 0 0 0 6-6H0zM26 0h18v22a14 14 0 0 1-14 14h-4v-8h4a6 6 0 0 0 6-6H26z"/></svg>
  </article>

  <div class="btn" style="left:490px;top:1398px;width:223px;height:51px">VIEW ALL FEEDACKS</div>
</section>

<section class="about">
  <div class="abs portrait" role="img" aria-label="Portrait photo of Peter Joseph Lindqvist"></div>
  <h2 class="abs heading section-title" style="left:136px;top:1532px">ABOUT</h2>
  <h2 class="abs heading section-title" style="left:136px;top:1595px">PETER JOSEPH <span class="gold">LINDQVIST</span></h2>
  <div class="abs gold" style="left:140px;top:1651px;font-size:18px;font-weight:700">Rooted Stillness® Teacher</div>
  <div class="rule" style="left:138px;top:1683px"></div>
  <p class="abs copy" style="left:136px;top:1693px;width:500px">Growing up in Scotland I had a strong connection with nature &amp; the outdoors. Playing outside with friends, with bikes, ball sports, and later mountaineering and rock climbing, was what most interested me.</p>
  <div class="abs gold" style="left:136px;top:1791px;font-size:18px;font-weight:700">Rooted Stillness Studies:</div>
  <div class="abs study" style="left:137px;top:1818px">Clear Living Mind®<br>Brain Mapping<br>Deep Field Healing®</div>
  <div class="btn" style="left:134px;top:1907px;width:200px;height:51px">BOOK A SESSION</div>
</section>

<footer>
  <svg class="abs footer-shape" width="1200" height="410" viewBox="0 0 1200 410">
    <path d="M0 96 Q600 -66 1200 96 L1200 410 L0 410Z" fill="#b8913c"/>
    <path d="M0 139 Q600 -93 1200 139 L1200 410 L0 410Z" fill="#e4dab9"/>
  </svg>
  <div class="abs footer-mark"></div>
  <div class="abs footer-brand"><div class="name">Peter Lindqvist</div></div>
  <nav class="abs footer-nav"><span>The Practice</span><span>About Me</span><span>Feedback</span><span>Approach</span><span>Contact Me</span></nav>
  <div class="abs divider" style="top:2250px"></div>

  <div class="abs contact" style="left:136px;top:2275px">
    <span class="icon-circle"><svg width="20" height="20" viewBox="0 0 24 24" fill="none" stroke="#1a1a1a" stroke-width="1.6"><path d="M12 22s7-7 7-12a7 7 0 0 0-14 0c0 5 7 12 7 12z"/><circle cx="12" cy="10" r="2.5"/></svg></span>
    <div>Rua das Flores 128b<br>Estrela, Lisbon, Portugal, 1200-195.</div>
  </div>
  <div class="abs contact" style="left:576px;top:2275px">
    <span class="icon-circle"><svg width="20" height="20" viewBox="0 0 24 24" fill="none" stroke="#1a1a1a" stroke-width="1.6"><path d="M5 3h4l2 5-2.5 1.5a11 11 0 0 0 6 6L16 13l5 2v4a2 2 0 0 1-2 2A16 16 0 0 1 3 5a2 2 0 0 1 2-2z"/></svg></span>
    <div>Call Us<br><strong>(+351) 91 204 7730</strong></div>
  </div>
  <div class="abs contact" style="left:845px;top:2275px">
    <span class="icon-circle" style="width:36px;height:36px"><svg width="18" height="18" viewBox="0 0 24 24" fill="none" stroke="#1a1a1a" stroke-width="1.6"><rect x="3" y="6" width="18" height="13"/><path d="M3 7l9 7 9-7"/></svg></span>
    <div>Email Us<br>info@peter-lindqvist.net</div>
  </div>

  <div class="abs divider" style="top:2347px"></div>
  <div class="abs" style="left:134px;top:2384px;font-size:14px;color:var(--ink)">© 2025 Peter Lindqvist. All Rights Reserved.</div>
  <div class="btn" style="left:559px;top:2373px;width:159px;height:46px">CONTACT ME</div>
  <div class="abs social" style="left:998px;top:2381px"></div>
  <div class="abs social" style="left:1037px;top:2381px"></div>
</footer>

</body>
</html>
```